Business card for a "family office" company

Please provide professional looking business card designs, incorporating the attached logo and below details. Harrowmere Holdings Pty Ltd is a family office / financial investment company. We are looking for a modern, professional and contemporary card design.

Industry/Entity Type

Finance

Contact Information for Business Card

Name: Dean Malcott
Title: Director
Company: Harrowmere Holdings Pty Ltd
Email: harrowlead@ozmailnet.com.au
Mobile: 0492 635 718
Address: 3/412 Bramwood Parade, Kelverton WA 6917, Australia

Requirements
Must have
• All details above and the logo. logo only on back side. incorporate colours of logo
Nice to have
• up to you
Should not have
• ?

```html
<!DOCTYPE html>
<html lang="en">
<head>
<meta charset="utf-8">
<title>Harrowmere Holdings – Business Card</title>
<link href="https://fonts.googleapis.com/css2?family=Cinzel:wght@400;600&family=Crimson+Text:wght@400;600;700&display=swap" rel="stylesheet">
<style>
  :root {
    --backdrop: #26262a;
    --navy: #1f1f5b;
    --navy-soft: #5a5aa6;
    --silver: #cfd0d6;
    --panel: #dcdce6;
    --paper: #ffffff;
  }
  * { margin: 0; padding: 0; box-sizing: border-box; }
  html, body { width: 1200px; height: 1200px; overflow: hidden; }
  body {
    background: var(--backdrop);
    position: relative;
    font-family: "Crimson Text", Georgia, serif;
  }
  .card {
    position: absolute;
    left: 150px;
    width: 900px;
    height: 514px;
    overflow: hidden;
  }
  .card--back { top: 70px; background: var(--navy); }
  .card--front { top: 616px; background: var(--paper); }

  .wordmark {
    font-family: "Cinzel", "Times New Roman", serif;
    font-weight: 600;
    text-align: center;
    letter-spacing: 0.16em;
    line-height: 1.15;
  }
  .card--back .wordmark {
    position: absolute;
    left: 0; right: 0; top: 190px;
    color: var(--silver);
    font-size: 52px;
  }
  .card--back .wordmark span { display: block; font-size: 30px; letter-spacing: 0.42em; }
  .mark-square {
    width: 46px; height: 46px;
    margin: 0 auto 18px;
    background: currentColor;
  }

  .front-panel {
    position: absolute;
    right: 0; top: 0;
    width: 320px; height: 100%;
    background: var(--panel);
  }
  .front-content {
    position: absolute;
    left: 40px; top: 58px;
    width: 600px;
    text-align: center;
    color: var(--navy);
  }
  .card--front .wordmark { font-size: 46px; color: var(--navy); }
  .card--front .wordmark span { display: block; font-size: 26px; letter-spacing: 0.42em; }
  .person-name {
    margin-top: 24px;
    font-family: "Cinzel", "Times New Roman", serif;
    font-weight: 600;
    font-size: 30px;
    letter-spacing: 0.05em;
  }
  .person-title {
    font-family: "Cinzel", "Times New Roman", serif;
    font-size: 18px;
    letter-spacing: 0.08em;
    color: var(--navy-soft);
    margin-bottom: 8px;
  }
  .phone { font-weight: 700; font-size: 24px; letter-spacing: 0.06em; }
  .email { font-size: 22px; }
  .address { font-size: 21px; white-space: nowrap; position: relative; z-index: 1; }
</style>
</head>
<body>
  <section class="card card--back" aria-label="Card back">
    <div class="wordmark">
      <div class="mark-square"></div>
      Harrowmere<span>Holdings</span>
    </div>
  </section>

  <section class="card card--front" aria-label="Card front">
    <div class="front-panel"></div>
    <div class="front-content">
      <div class="wordmark">
        <div class="mark-square"></div>
        Harrowmere<span>Holdings</span>
      </div>
      <p class="person-name">DEAN MALCOTT</p>
      <p class="person-title">DIRECTOR</p>
      <p class="phone">0492 635 718</p>
      <p class="email">harrowlead@ozmailnet.com.au</p>
      <p class="address">3/412 Bramwood Parade, Kelverton WA 6917, Australia</p>
    </div>
  </section>
</body>
</html>
```